Mortgage Loan Program(s) for Furloughed Federal Government Workers

Mortgage Loan Program(s)
For
Furloughed Federal Government Workers

* Preserve Your Credit Rating
* Receive Cash out to Increase Savings or Consolidate Bills
* Close in 30 Days or Less
* FHA and Conventional Loan Programs
* Very Competitive Rates Available
* DC & MD Properties Only

You deserve better. Contact us today....

Office (800) 446-2917 x24
Cell (240) 958-2043
Email mpelton@brightkeyhome.example

Marcus Pelton
Brightkey Financial Services, Inc.
NMLS #518374 / #60471

Target Market(s)

```html
<!DOCTYPE html>
<html lang="en">
<head>
<meta charset="utf-8">
<title>Mortgage Loan Program(s) for Furloughed Federal Government Workers</title>
<link rel="stylesheet" href="https://fonts.googleapis.com/css2?family=Lato:wght@300;400;700;900&family=Lora:ital@1&family=Playfair+Display:ital,wght@1,600&family=Roboto+Condensed:wght@700&display=swap">
<style>
  :root {
    --green: #16913c;
    --blue: #1c57a6;
    --navy: #1f3f93;
    --panel: #f1f1f1;
    --ink: #3a3a3a;
    --white: #ffffff;
    --bg: #e4e4e4;
  }
  * { box-sizing: border-box; margin: 0; padding: 0; }
  html, body { width: 1200px; height: 960px; overflow: hidden; background: var(--bg); }
  .flyer {
    position: absolute; left: 273px; top: 20px;
    width: 612px; height: 860px;
    transform: scale(1.07); transform-origin: top left;
    background: var(--white); overflow: hidden;
    font-family: "Lato", sans-serif;
  }
  .abs { position: absolute; }
  .backdrop { left: 0; top: 0; width: 612px; height: 860px; }
  .hero-photo {
    left: 0; top: 0; width: 612px; height: 345px;
    background: radial-gradient(circle at 50% 55%, #fff2d0 0%, #e0a14a 12%, #7a4a22 35%, #2d1c10 65%, #120c08 100%);
    clip-path: polygon(8px 0, 612px 0, 612px 238px, 410px 345px, 230px 345px);
  }
  .logo-panel { left: 0; top: 118px; width: 230px; height: 196px; }
  .brand {
    left: 24px; top: 186px; width: 118px;
    display: flex; align-items: center; gap: 7px;
    font-family: "Lato", sans-serif; font-weight: 700; font-size: 12px; line-height: 1.2;
    color: var(--blue);
  }
  .brand-dot { flex: none; width: 20px; height: 20px; border-radius: 50%; background: #c9a64a; }
  .content {
    left: 4px; top: 340px; width: 428px; height: 400px;
    background: var(--panel);
    border-top-right-radius: 42px;
    border-right: 6px solid var(--green);
  }
  .title {
    left: 0; top: 380px; width: 436px; text-align: center;
    font-weight: 900; font-size: 39px; line-height: 46px; letter-spacing: -0.3px;
  }
  .title .l1 { color: var(--green); display: block; }
  .title .l2 { color: var(--blue); display: block; }
  .subtitle {
    left: 0; top: 472px; width: 436px; text-align: center;
    font-family: "Lora", serif; font-style: italic; font-size: 20px; line-height: 27px;
  }
  .subtitle .for { color: var(--green); display: block; }
  .subtitle .who { color: var(--blue); display: block; }
  .rule { left: 188px; top: 530px; width: 64px; height: 1px; background: #555; }
  .features-head {
    left: 0; top: 565px; width: 436px; text-align: center;
    font-weight: 300; font-size: 19px; color: var(--green);
  }
  .features { left: 28px; top: 606px; width: 390px; list-style: none; display: grid; grid-template-columns: 200px 190px; row-gap: 10px; }
  .feature {
    display: flex; align-items: center; gap: 10px; height: 30px;
    font-family: "Lora", serif; font-style: italic; font-size: 10.5px; line-height: 12px; color: var(--ink);
  }
  .icon { flex: none; width: 30px; height: 30px; }
  .cta {
    left: 0; top: 738px; width: 432px; height: 44px;
    background: var(--green); border-top-right-radius: 6px;
    font-family: "Playfair Display", serif; font-style: italic; font-weight: 600;
    font-size: 23px; color: var(--white); line-height: 44px; padding-left: 28px;
    letter-spacing: -0.4px; white-space: nowrap;
  }
  .signoff {
    left: 4px; top: 782px; width: 426px; height: 48px;
    background: var(--panel); border-bottom-right-radius: 30px;
    border-right: 6px solid var(--green); border-bottom: 4px solid var(--green);
    font-size: 14px; line-height: 40px; padding-left: 24px; color: #555; white-space: nowrap;
  }
  .signoff strong { color: var(--blue); font-weight: 700; }
  .signoff .sep { color: var(--blue); }
  .side-photo { left: 450px; width: 144px; }
  .photo-help { top: 274px; height: 168px; background: linear-gradient(160deg, #d9d4cc, #8c7a6a 55%, #4c3e36); clip-path: polygon(0 26%, 100% 0, 100% 100%, 0 100%); }
  .photo-couple { top: 452px; height: 178px; background: linear-gradient(170deg, #cfc7bd, #6d5a4c 50%, #3b3230); clip-path: polygon(0 0, 100% 0, 100% 60%, 0 100%); }
  .photo-portrait { top: 582px; height: 153px; background: linear-gradient(160deg, #4d6f9c, #1e3c6a 55%, #151c28); clip-path: polygon(0 30%, 100% 0, 100% 100%, 0 100%); }
  .contacts { left: 446px; top: 750px; width: 160px; list-style: none; font-family: "Roboto Condensed", sans-serif; font-weight: 700; color: var(--white); }
  .contacts li { display: flex; align-items: center; gap: 9px; height: 21px; font-size: 11.5px; white-space: nowrap; }
  .contacts li.email { font-size: 8.6px; letter-spacing: -0.1px; }
  .contacts svg { width: 13px; height: 13px; flex: none; }
</style>
</head>
<body>
<main class="flyer">
  <svg class="abs backdrop" viewBox="0 0 612 860" aria-hidden="true">
    <polygon points="0,12 8,0 230,345 200,345" fill="#16913c"/>
    <polygon points="445,345 612,238 612,262 470,345" fill="#16913c"/>
    <polygon points="432,585 612,585 612,860 0,860 0,830 432,760" fill="#1f3f93"/>
    <polygon points="440,590 612,528 612,585 440,640" fill="#ffffff"/>
    <polygon points="0,860 0,830 60,860" fill="#16913c"/>
    <polygon points="520,860 612,820 612,860" fill="#16913c"/>
    <polygon points="0,340 4,340 4,860 0,860" fill="#16913c"/>
  </svg>

  <div class="abs hero-photo" role="img" aria-label="Silhouette of a person with arms raised at the sunlit end of a stone tunnel"></div>

  <svg class="abs logo-panel" viewBox="0 0 230 196" aria-hidden="true">
    <polygon points="0,0 113,0 228,196 0,196" fill="#16913c"/>
    <polygon points="0,0 110,0 222,190 0,190" fill="#1c57a6"/>
    <polygon points="14,4 108,4 214,186 14,186" fill="#ffffff"/>
  </svg>
  <div class="abs brand"><span class="brand-dot"></span><span>Brightkey Financial Services, Inc.</span></div>

  <section class="abs content"></section>
  <h1 class="abs title"><span class="l1">MORTGAGE LOAN</span><span class="l2">PROGRAM(S)</span></h1>
  <p class="abs subtitle"><span class="for">For</span><span class="who">Furloughed Federal Government Workers</span></p>
  <div class="abs rule"></div>

  <h2 class="abs features-head">Our Features</h2>
  <ul class="abs features">
    <li class="feature">
      <svg class="icon" viewBox="0 0 30 30"><circle cx="15" cy="15" r="14" fill="#1c57a6"/><path d="M8 17a7 7 0 0 1 14 0" fill="none" stroke="#fff" stroke-width="1.8"/><path d="M15 17l3-4" stroke="#fff" stroke-width="1.8"/></svg>
      Preserve Your Credit Rating
    </li>
    <li class="feature">
      <svg class="icon" viewBox="0 0 30 30"><circle cx="15" cy="15" r="14" fill="#1c57a6"/><rect x="9" y="10" width="12" height="10" rx="1.5" fill="none" stroke="#fff" stroke-width="1.6"/><path d="M12 15l2 2 4-4" fill="none" stroke="#fff" stroke-width="1.6"/></svg>
      FHA and Conventional Loan Programs
    </li>
    <li class="feature">
      <svg class="icon" viewBox="0 0 30 30"><circle cx="15" cy="15" r="14" fill="#1c57a6"/><rect x="10" y="8" width="10" height="14" rx="1" fill="none" stroke="#fff" stroke-width="1.6"/><path d="M13 13h4M13 17h4" stroke="#fff" stroke-width="1.4"/></svg>
      Receive Cash out to Increase Savings or Consolidate Bills
    </li>
    <li class="feature">
      <svg class="icon" viewBox="0 0 30 30"><circle cx="15" cy="15" r="14" fill="#1c57a6"/><path d="M8 15l7-6 7 6h-2v6h-4v-4h-2v4h-4v-6z" fill="#fff"/></svg>
      DC &amp; MD Properties Only
    </li>
    <li class="feature">
      <svg class="icon" viewBox="0 0 30 30"><circle cx="15" cy="15" r="14" fill="#1c57a6"/><text x="15" y="18" text-anchor="middle" font-family="Roboto Condensed, sans-serif" font-weight="700" font-size="13" fill="#fff">30</text><text x="15" y="24" text-anchor="middle" font-family="Lato, sans-serif" font-size="4.5" fill="#fff">Days</text></svg>
      Close in 30 Days or Less
    </li>
    <li class="feature">
      <svg class="icon" viewBox="0 0 30 30"><circle cx="15" cy="15" r="14" fill="#1c57a6"/><rect x="9" y="15" width="3" height="6" fill="#fff"/><rect x="13.5" y="12" width="3" height="9" fill="#fff"/><rect x="18" y="14" width="3" height="7" fill="#fff"/><circle cx="15" cy="9" r="1.5" fill="#fff"/></svg>
      Very Competitive Rates Available
    </li>
  </ul>

  <p class="abs cta">You deserve better. Contact us today....</p>
  <p class="abs signoff"><strong>Marcus Pelton</strong> <span class="sep">|</span> Brightkey Financial Services, Inc. <span class="sep">|</span> NMLS</p>

  <div class="abs side-photo photo-help" role="img" aria-label="Worried couple reviewing bills, one holding a help sign"></div>
  <div class="abs side-photo photo-couple" role="img" aria-label="Couple sitting together reading a letter"></div>
  <div class="abs side-photo photo-portrait" role="img" aria-label="Portrait of the loan officer in a suit"></div>

  <ul class="abs contacts">
    <li><svg viewBox="0 0 14 14"><path d="M3 1l2.5 3-1.3 1.5a8 8 0 0 0 4.3 4.3L10 8.5 13 11l-1.5 2C6 13 1 8 1 2.5z" fill="#fff"/></svg>(800) 446-2917 x24</li>
    <li><svg viewBox="0 0 14 14"><rect x="3.5" y="0.5" width="7" height="13" rx="1.2" fill="none" stroke="#fff" stroke-width="1.3"/><circle cx="7" cy="11" r="0.8" fill="#fff"/></svg>(240) 958-2043</li>
    <li class="email"><svg viewBox="0 0 14 14"><rect x="1" y="3" width="12" height="8" fill="#fff"/><path d="M1 3l6 5 6-5" fill="none" stroke="#1f3f93" stroke-width="1"/></svg>mpelton@brightkeyhome.example</li>
  </ul>
</main>
</body>
</html>
```